Patient Fact sheets for medical conditions and treatments

Hi,

I need a new design for my patient fact sheets. I am moving from my current clinic and I am looking from a new look.

I have attached
1. a current Fact sheet
2. New home page to the website
3. New Logo.

They need to be single page and easily readable for patients.

The will be in both PDF and print form in the future.

Target Market(s)

Patients with chronic pain age 40+

Font styles to use
Serif

Requirements
Must have
• My logo, should be inline with design elements on the Front page provided.

Please use the same font as the Logo

```html
<!DOCTYPE html>
<html lang="en">
<head>
<meta charset="utf-8">
<title>Fact Sheet – Platelet Rich Plasma (PRP) Therapy</title>
<link rel="stylesheet" href="https://fonts.googleapis.com/css2?family=Roboto+Slab:wght@800&family=Source+Sans+3:wght@400;600;700&display=swap">
<style>
:root{
  --teal:#00a3b1;
  --teal-dark:#008c99;
  --orange:#f5a511;
  --ink:#2e2e2e;
  --grey:#3c3c3c;
  --page:#f1f1ef;
  --white:#ffffff;
}
*{box-sizing:border-box;margin:0;padding:0}
html,body{width:1200px;height:2237px;overflow:hidden}
body{background:var(--page);font-family:"Source Sans 3",Arial,sans-serif;color:var(--grey)}
.sheet-frame{position:absolute;left:40px;top:327px;width:1120px;height:1583px;box-shadow:0 6px 24px rgba(0,0,0,.18)}
.sheet{position:absolute;left:0;top:0;width:901px;height:1273px;background:var(--white);transform:scale(1.2431);transform-origin:0 0;overflow:hidden}
.abs{position:absolute}

/* header */
.hero-bg{left:0;top:0}
.brand{left:46px;top:72px;font-weight:400;font-size:42px;line-height:1;color:#3a3f45;letter-spacing:-.5px;display:flex;align-items:center;gap:10px}
.brand-mark{width:16px;height:16px;background:var(--teal)}
.kicker{left:408px;top:44px;font-family:"Source Sans 3",sans-serif;font-weight:600;font-size:29px;letter-spacing:1px;color:var(--orange)}
.title{left:408px;top:82px;font-family:"Roboto Slab",Georgia,serif;font-weight:800;font-size:36px;line-height:45px;color:var(--white)}

.intro{left:44px;top:206px;width:250px;color:var(--white)}
.intro h2{font-size:21px;font-weight:700;letter-spacing:.3px}
.intro-rule{display:block;width:26px;height:3px;background:var(--white);margin:10px 0 11px}
.intro p{font-size:13.2px;line-height:16.4px}

/* section tags */
.tag{position:relative;display:inline-block;margin-left:7px;background:var(--teal);color:var(--white);font-weight:700;font-size:20px;line-height:22px;text-transform:uppercase;padding:5px 24px 5px 11px;border-radius:0 17px 17px 0}
.tag::before{content:"";position:absolute;left:-7px;top:-4px;bottom:-4px;width:3px;background:var(--orange)}
.tag::after{content:"";position:absolute;right:-5px;top:-3px;bottom:-3px;width:36px;border:2px solid var(--orange);border-left:none;border-radius:0 21px 21px 0}

.body-copy{font-size:12.8px;line-height:16.3px;color:var(--grey)}

.col-left{left:42px;width:360px}
.col-right{left:428px;width:440px}

.lead{font-weight:700;font-size:15.6px;line-height:19px;color:var(--ink)}
.ticks{list-style:none}
.ticks li{position:relative;padding-left:26px;font-size:12.9px;line-height:16px;color:var(--grey)}
.ticks svg{position:absolute;left:2px;top:3px;width:11px;height:11px}

.treat-grid{display:grid;grid-template-columns:158px 134px 140px;row-gap:10px}
.treat-grid li{padding-left:20px}
.treat-grid svg{left:0}

.ask{font-weight:700;font-size:16px;line-height:19px;color:var(--ink)}
.disclaimer h3{font-size:11px;font-weight:700;color:var(--teal);letter-spacing:.2px}
.disclaimer p{font-size:7.6px;line-height:9.4px;color:var(--grey);margin-top:3px}

.more-info{left:42px;top:1153px;font-weight:700;font-size:15.5px;color:var(--teal)}

/* footer */
.footer{left:0;top:1183px;width:901px;height:90px}
.phones{left:44px;top:1193px;color:var(--white);font-weight:700;font-size:20.5px;line-height:25px}
.phones div{display:flex;align-items:center;gap:12px}
.phones svg{width:18px;height:18px}
.address{left:314px;top:1200px;color:var(--white);font-size:15.5px;line-height:19.5px;display:flex;gap:8px}
.address svg{width:12px;height:17px;margin-top:2px}
.divider{left:617px;top:1196px;width:1px;height:58px;background:var(--white)}
.contact{left:634px;top:1200px;color:var(--white);font-size:15.5px;line-height:19.5px}
.contact .row{display:flex;align-items:center;gap:8px}
.contact svg{width:14px;height:11px}
.socials{display:inline-flex;gap:9px;margin-left:12px;vertical-align:middle}
.socials span{width:11px;height:11px;border:2px solid var(--white);border-radius:2px;display:block}
</style>
</head>
<body>
<svg width="0" height="0" style="position:absolute">
  <symbol id="tick" viewBox="0 0 12 12">
    <rect x="0.8" y="2" width="9" height="9" rx="1.2" fill="none" stroke="#00a3b1" stroke-width="1.4"/>
    <path d="M2.8 6.3 L5 8.6 L11.2 1.4" fill="none" stroke="#00a3b1" stroke-width="1.6" stroke-linecap="round" stroke-linejoin="round"/>
  </symbol>
</svg>

<div class="sheet-frame">
<main class="sheet">

  <svg class="abs hero-bg" width="901" height="512" viewBox="0 0 901 512">
    <rect width="901" height="512" fill="#00a3b1"/>
    <path d="M0 0 H382 C372 108 322 192 214 195 H0 Z" fill="#ffffff"/>
    <defs>
      <linearGradient id="photoTone" x1="0" y1="0" x2="1" y2="1">
        <stop offset="0" stop-color="#d9e6ee"/>
        <stop offset="0.5" stop-color="#b7cad6"/>
        <stop offset="1" stop-color="#8fa8b8"/>
      </linearGradient>
    </defs>
    <path role="img" aria-label="Photo: a doctor in a white coat examining the knee of a seated older woman in a bright clinic room" d="M402 192 H901 V512 H418 C350 470 322 400 330 340 C338 270 362 214 402 192 Z" fill="url(#photoTone)"/>
  </svg>

  <div class="abs brand"><span>northvale pain</span><span class="brand-mark"></span></div>
  <div class="abs kicker">FACT SHEET</div>
  <h1 class="abs title">Platelet Rich Plasma (PRP)<br>Therapy</h1>

  <section class="abs intro">
    <h2>WHAT IS PRP?</h2>
    <span class="intro-rule"></span>
    <p>Platelet-Rich Plasma (PRP) is concentrated platelets and white blood cells derived from your own blood. Platelet Rich Plasma Injection Therapy (PRP therapy), is a growing treatment approach for soft tissue injuries including tendon, muscle and ligaments. It is also showing good results for mild to moderate osteoarthritis. While this approach has been used overseas for many years, it’s fairly new to Australia in the treatment of musculoskeletal and orthopaedic conditions.</p>
  </section>

  <section class="abs col-left" style="top:540px">
    <h2 class="tag">How does PRP work?</h2>
    <p class="body-copy" style="margin-top:12px">Some tissues in the body have a poor blood supply or respond poorly to excessive load, ultimately failing to heal naturally. While some of our primary treatment such as physiotherapy, massage, biomechanical correction and other forms of treatment are used to treat these soft tissue injuries, sometimes the body fails to respond. PRP therapy utilises the healing properties in blood to allow a healing reaction to occur in a tissue that’s not healing on its own. Our blood has small granules called ‘platelets’, which contain special growth factors that when released, allow stem cells in the particular tissue to ‘switch’ on and cause new tissue to be created and heal the injured area. Take the example of achilles tendinopathy. If the achilles is painful, thickened and not responding to rehabilitation, then the sports physician will inject the PRP into the achilles which will cause the tendon cells (tenocytes/fibroblasts) to create new achilles collagen to strengthen the achilles. White blood cells also enter the area to mop up any achilles tissue that may have been damaged due to the ongoing pain and thickening in the area.</p>
  </section>

  <section class="abs col-left" style="top:912px">
    <h2 class="tag">What are the expected<br>results of PRP?</h2>
    <p class="body-copy" style="margin-top:16px;padding-left:4px">Because the goal of PRP therapy is to resolve pain through healing, it could prove to have lasting results. Initial improvement may be seen within a few weeks, gradually increasing as the healing progresses. Research studies and clinical practice have shown PRP therapy to be very effective at relieving pain and returning patients to their normal lives. The need for surgery can also be greatly reduced by treating injured tissues before the damage progresses and the condition is irreversible.</p>
  </section>

  <div class="abs more-info">For more information:</div>

  <section class="abs col-right" style="top:539px">
    <h2 class="tag">Role of platelets &amp; growth factors</h2>
    <p class="lead" style="margin:11px 0 0 7px;width:410px">PRP contains highly concentrated platelets. Platelets have been identified to secrete growth factors, which are known to play a role in:</p>
    <ul class="ticks" style="margin-top:16px">
      <li style="margin-bottom:11px"><svg><use href="#tick"/></svg>Increasing tissue vascularity and increasing the rate of epithelial tissue</li>
      <li style="margin-bottom:11px"><svg><use href="#tick"/></svg>production (wound healing) Attracting other cells that fight infection</li>
      <li style="margin-bottom:11px"><svg><use href="#tick"/></svg>Acting as a seal during closures</li>
      <li style="margin-bottom:11px"><svg><use href="#tick"/></svg>Oroviding an immediate surgical hemostatic agent (reduction of bleeding)</li>
      <li><svg><use href="#tick"/></svg>Osteogenesis (bone regeneration and repair)</li>
    </ul>
  </section>

  <section class="abs col-right" style="top:840px">
    <h2 class="tag">What can PRP treat?</h2>
    <p class="lead" style="margin-top:10px">PRP therapy can be used for:</p>
    <ul class="ticks treat-grid" style="margin-top:14px">
      <li><svg><use href="#tick"/></svg>Orthopedic surgery</li>
      <li><svg><use href="#tick"/></svg>Cardiac surgery</li>
      <li><svg><use href="#tick"/></svg>Plastic and cosmetic surgery</li>
      <li><svg><use href="#tick"/></svg>Ear, nose, throat (ENT) surgery</li>
      <li><svg><use href="#tick"/></svg>Oral maxillofacial</li>
      <li style="padding-top:18px"><svg style="top:21px"><use href="#tick"/></svg>Neurosurgery</li>
      <li><svg><use href="#tick"/></svg>Vascular surgery</li>
      <li><svg><use href="#tick"/></svg>Wound healing</li>
      <li><svg><use href="#tick"/></svg>Burn care.</li>
    </ul>
    <p class="ask" style="margin-top:20px">Ask your doctor whether plateletrich plasma is<br>appropriate for your surgical procedure</p>
    <div class="disclaimer" style="margin-top:22px;width:430px">
      <h3>DISCLAIMER</h3>
      <p>Please note the contents contained in this Patient Fact Sheet are not intended as a substitute for your own independent health professional’s advice, diagnosis or treatment. At Northvale Pain Clinic, we assess every patient’s condition individually. As leaders in pain intervention, we aim to provide advanced, innovative, and evidence-based treatments tailored to suit each patient. As such, recommended treatments and their outcomes will vary from patient to patient. If you would like to find out whether our treatments are suitable for your specific condition, please speak to one of our doctors at the time of your consultation.</p>
    </div>
  </section>

  <svg class="abs footer" viewBox="0 0 901 90">
    <rect width="901" height="90" fill="#00a3b1"/>
    <path d="M0 0 H262 C292 20 294 70 262 90 H0 Z" fill="#f5a511"/>
    <path d="M270 0 C302 22 304 68 272 90" fill="none" stroke="#f5a511" stroke-width="3"/>
  </svg>

  <div class="abs phones">
    <div><svg viewBox="0 0 20 20"><path d="M4 2 L7.5 2 L9 6 L7 7.6 C8 10 10 12 12.4 13 L14 11 L18 12.5 L18 16 C18 17 17 18 16 18 C8.5 17.5 2.5 11.5 2 4 C2 3 3 2 4 2 Z" fill="#fff"/><path d="M12 2.5 A6 6 0 0 1 17.5 8 M12 5.5 A3 3 0 0 1 14.5 8" fill="none" stroke="#fff" stroke-width="1.5"/></svg>03 9000 1234</div>
    <div><svg viewBox="0 0 20 20"><rect x="5" y="2" width="10" height="5" fill="#fff"/><rect x="2" y="8" width="16" height="7" rx="1.5" fill="#fff"/><rect x="5" y="13" width="10" height="5" fill="#fff" stroke="#f5a511" stroke-width="1"/></svg>03 9000 1235</div>
  </div>

  <div class="abs address">
    <svg viewBox="0 0 12 17"><path d="M6 0.5 C9.2 0.5 11.5 2.9 11.5 6 C11.5 10 6 16.5 6 16.5 C6 16.5 0.5 10 0.5 6 C0.5 2.9 2.8 0.5 6 0.5 Z" fill="#fff"/><circle cx="6" cy="6" r="2.2" fill="#00a3b1"/></svg>
    <div>Northvale Pain Clinic Harbour House,<br>Ground Floor 48 Elm Road</div>
  </div>

  <div class="abs divider"></div>

  <div class="abs contact">
    <div class="row"><svg viewBox="0 0 14 11"><rect x="0.5" y="0.5" width="13" height="10" fill="#fff"/><path d="M0.5 0.8 L7 6 L13.5 0.8" fill="none" stroke="#00a3b1" stroke-width="1.2"/></svg>info@northvalepain.example</div>
    <div class="row">northvalepain.example<span class="socials"><span></span><span></span><span></span></span></div>
  </div>

</main>
</div>
</body>
</html>
```